SEO AND WEB DESIGN COMPANY BUSINESS CARD DESIGN

I need an eye catching , simple business card design that will match my logo . I need 2 versions of it ( white background and black background) - SOME PEOPLE DID NOT GET IT AND SENDING US FRONT WHITE BACK WHITE VERSIONS WHICH IS NOT CORRECT.

ONE VERSION SHOULD BE BACK AND FRONT ALL BLACK , SECOND VERSION SHOULD BE BACK AND FRONT ALL WHITE

logo psd files are attached for both versions. The business card is going to have : First Name- Last name - position - phone numbers

```html
<!DOCTYPE html>
<html lang="en">
<head>
<meta charset="utf-8">
<title>Northpeak Studio – Business Cards (Black Version)</title>
<link rel="stylesheet" href="https://fonts.googleapis.com/css2?family=Oswald:wght@500;600&family=Lato:wght@400;700&display=swap">
<style>
  :root {
    --surface: #dcdcdc;
    --card: #050505;
    --ink: #ffffff;
    --ink-soft: #d9d9d9;
    --accent: #3b8fe8;
    --rule: #8a8a8a;
  }
  * { box-sizing: border-box; margin: 0; padding: 0; }
  html, body {
    width: 1200px;
    height: 900px;
    overflow: hidden;
    background: var(--surface);
  }
  .sheet {
    position: relative;
    width: 1200px;
    height: 900px;
  }
  .card {
    position: absolute;
    width: 560px;
    height: 320px;
    background: var(--card);
    border-radius: 28px;
    color: var(--ink);
    display: flex;
    flex-direction: column;
    align-items: center;
    box-shadow: 0 6px 18px rgba(0, 0, 0, 0.25);
  }
  .card--front { left: 90px; top: 120px; }
  .card--back  { left: 550px; top: 460px; }

  .brand {
    display: flex;
    align-items: center;
    gap: 14px;
  }
  .brand__dot {
    width: 30px;
    height: 30px;
    border-radius: 50%;
    background: var(--accent);
  }
  .brand__name {
    font-family: "Oswald", sans-serif;
    font-weight: 600;
    font-size: 50px;
    letter-spacing: 1px;
    color: var(--ink);
    line-height: 1;
  }

  .card--front .brand { margin-top: 112px; }
  .address {
    margin-top: auto;
    margin-bottom: 48px;
    font-family: "Lato", sans-serif;
    font-size: 15px;
    letter-spacing: 0.3px;
    color: var(--ink);
  }

  .card--back .brand { margin-top: 46px; }
  .person {
    margin-top: 26px;
    text-align: center;
  }
  .person__name {
    font-family: "Oswald", sans-serif;
    font-weight: 600;
    font-size: 22px;
    letter-spacing: 0.5px;
    text-transform: uppercase;
    line-height: 1.1;
  }
  .person__role {
    font-family: "Lato", sans-serif;
    font-size: 15px;
    color: var(--ink-soft);
  }
  .divider {
    width: 180px;
    height: 1px;
    background: var(--rule);
    margin: 14px 0 12px;
  }
  .contact {
    list-style: none;
    font-family: "Lato", sans-serif;
    font-size: 15px;
    line-height: 1.55;
    text-align: center;
    color: var(--ink);
  }
  .contact__label { font-weight: 700; }
  .contact__sep { margin: 0 8px; color: var(--ink-soft); }
</style>
</head>
<body>
<main class="sheet">

  <section class="card card--front" aria-label="Card front">
    <div class="brand">
      <span class="brand__dot" aria-hidden="true"></span>
      <span class="brand__name">NORTHPEAK STUDIO</span>
    </div>
    <p class="address">48 Harbour Lane, Westfield Bay, Marlow, 204817.</p>
  </section>

  <section class="card card--back" aria-label="Card back">
    <div class="brand">
      <span class="brand__dot" aria-hidden="true"></span>
      <span class="brand__name">NORTHPEAK STUDIO</span>
    </div>
    <div class="person">
      <p class="person__name">Daniel Reyes</p>
      <p class="person__role">Managing Director</p>
    </div>
    <div class="divider" aria-hidden="true"></div>
    <ul class="contact">
      <li><span class="contact__label">P:</span> 061-482 730 915<span class="contact__sep">|</span><span class="contact__label">E:</span> hello@northpeakstudio.com</li>
      <li><span class="contact__label">W:</span> www.northpeakstudio.com</li>
    </ul>
  </section>

</main>
</body>
</html>
```